Mobile digital movie retailer needs design for rewards program app

We would like designs for an 1-page Android app that allows users to rent new release movies and promotes loyalty through a rewards program. The rewards program should have 5-6 tiers -- users earn points for each movie they rent. Users in higher tiers get special offers like free rentals and early access to upcoming titles.
We only offer 5-10 movies at a single time, so there's no need for a sorting or filtering. A simple list will do.
The designs should communicate the following: user's current tier, how close the user is to achieving the next tier, # of movies the user has purchased (and other relevant stats).
Digital

```html
<!DOCTYPE html>
<html lang="en">
<head>
<meta charset="UTF-8">
<title>Rewards – Rent Movies</title>
<link href="https://fonts.googleapis.com/css2?family=Roboto:wght@100;300;400&display=swap" rel="stylesheet">
<style>
  :root{
    --bar-top:#35b2e8;
    --bar-bottom:#0a78bd;
    --panel:#2c2c2c;
    --panel-line:#5a5a5a;
    --accent-blue:#22a4e3;
    --level-teal:#45e6cf;
    --muted:#a8a8a8;
    --list-bg:#ffffff;
    --separator:#1e2b38;
    --title:#1a1a1a;
    --genre:#6e6e6e;
    --rent:#3cc24a;
  }
  *{box-sizing:border-box;margin:0;padding:0}
  html,body{width:677px;height:1200px;overflow:hidden;background:var(--list-bg)}
  body{position:relative;font-family:"Roboto",Arial,sans-serif}

  .app-bar{position:absolute;left:0;top:0;width:677px;height:63px;
    background:linear-gradient(var(--bar-top),var(--bar-bottom))}
  .menu-icon{position:absolute;left:16px;top:12px}

  .stats{position:absolute;left:0;top:63px;width:677px;height:309px;background:var(--panel)}
  .stats::after{content:"";position:absolute;left:0;bottom:-5px;width:100%;height:5px;background:var(--accent-blue)}
  .stat-divider-v{position:absolute;left:338px;top:0;width:2px;height:309px;background:var(--panel-line)}
  .stat-divider-h{position:absolute;left:340px;top:155px;width:337px;height:2px;background:var(--panel-line)}

  .level{position:absolute;left:0;top:0;width:338px;height:309px;text-align:center}
  .level-label{position:absolute;left:0;right:0;top:38px;font-size:22px;font-weight:300;color:var(--accent-blue)}
  .level-value{position:absolute;left:0;right:0;top:32px;font-size:290px;font-weight:100;line-height:1;
    color:var(--level-teal);text-shadow:0 0 14px rgba(69,230,207,.7)}

  .stat{position:absolute;left:340px;width:337px;text-align:center}
  .stat-label{font-size:24px;font-weight:300;color:var(--muted)}
  .stat-value{font-size:44px;font-weight:300;color:var(--accent-blue);line-height:1.1}
  .stat--rented{top:40px}
  .stat--points{top:188px;padding-left:60px}
  .award-icon{position:absolute;left:383px;top:258px}

  .movie-list{position:absolute;left:0;top:377px;width:677px;list-style:none}
  .movie{position:relative;height:172px;border-top:8px solid var(--separator)}
  .movie:first-child{border-top:none;height:164px}
  .poster{position:absolute;left:18px;top:6px;width:95px;height:152px}
  .movie-title{position:absolute;left:130px;top:4px;font-size:36px;font-weight:400;color:var(--title)}
  .movie-genre{position:absolute;left:132px;top:46px;font-size:24px;font-weight:300;color:var(--genre)}
  .rent-button{position:absolute;right:20px;bottom:16px;font-size:35px;font-weight:300;color:var(--rent);letter-spacing:1px}
</style>
</head>
<body>
  <header class="app-bar">
    <svg class="menu-icon" width="52" height="40" viewBox="0 0 52 40" aria-label="Menu">
      <rect x="0" y="2" width="52" height="7" rx="1" fill="#fff"/>
      <rect x="0" y="17" width="52" height="7" rx="1" fill="#fff"/>
      <rect x="0" y="32" width="52" height="7" rx="1" fill="#fff"/>
    </svg>
  </header>

  <section class="stats">
    <div class="level">
      <div class="level-label">level</div>
      <div class="level-value">3</div>
    </div>
    <div class="stat-divider-v"></div>
    <div class="stat-divider-h"></div>
    <div class="stat stat--rented">
      <div class="stat-label">rented movies</div>
      <div class="stat-value">54</div>
    </div>
    <div class="stat stat--points">
      <div class="stat-label">total points</div>
      <div class="stat-value">10985</div>
    </div>
  </section>
  <svg class="award-icon" width="40" height="70" viewBox="0 0 40 70" aria-label="Points award">
    <path d="M10 30 L4 64 L13 58 L18 67 L20 38 Z" fill="#fff"/>
    <path d="M30 30 L36 64 L27 58 L22 67 L20 38 Z" fill="#fff"/>
    <circle cx="20" cy="20" r="18" fill="#fff"/>
    <circle cx="20" cy="20" r="12" fill="none" stroke="#2c2c2c" stroke-width="3"/>
  </svg>

  <ul class="movie-list">
    <li class="movie">
      <div class="poster" role="img" aria-label="Poster for Full Throttle" style="background:linear-gradient(#0c1e3a,#1d5f9a 55%,#0a1528)"></div>
      <div class="movie-title">Full Throttle</div>
      <div class="movie-genre">Action</div>
      <div class="rent-button">RENT</div>
    </li>
    <li class="movie">
      <div class="poster" role="img" aria-label="Poster for The Crimson Weaver 2" style="background:linear-gradient(#5a6f88,#2d3b52 50%,#8a1c22)"></div>
      <div class="movie-title">The Crimson Weaver 2</div>
      <div class="movie-genre">Action</div>
      <div class="rent-button">RENT</div>
    </li>
    <li class="movie">
      <div class="poster" role="img" aria-label="Poster for The Broker of Harbor Street" style="background:linear-gradient(#e9e3d4,#b59a6a 45%,#3a3530)"></div>
      <div class="movie-title">The Broker of Harbor Street</div>
      <div class="movie-genre">drama</div>
      <div class="rent-button">RENT</div>
    </li>
    <li class="movie">
      <div class="poster" role="img" aria-label="Poster for Sentinel Rising 2" style="background:linear-gradient(#a8b4bf,#4b5d70 50%,#1b2530)"></div>
      <div class="movie-title">Sentinel Rising 2</div>
      <div class="movie-genre">action</div>
      <div class="rent-button">RENT</div>
    </li>
    <li class="movie">
      <div class="poster" role="img" aria-label="Poster for Leviathan" style="background:linear-gradient(#7a1a14,#c2472a 50%,#3a0d0a)"></div>
      <div class="movie-title">Leviathan</div>
      <div class="movie-genre">action</div>
      <div class="rent-button">RENT</div>
    </li>
  </ul>
</body>
</html>
```